VFX Company Business Card Design Project

The Ember Vale is a decentralized Visual Effects Studio servicing the television and feature film industries.
Project Brief:
Take our logo that was previously designed on Pixel Harbor and make a double sided business card.
Requirements:
- Card MUST be double sided.
- Front of card MUST have the yellow part of our logo against the dark grey background.
- Back of card is completely up to the designer.
- Back of card must include the complete company logo.
Please follow these File Preparation guidelines:
http://printmoor.example/infopage?file=filetype_en&s=PrintMoor_new&lang=en
Industry/Entity Type
Business
Look and feel
Each slider illustrates characteristics of the customer's brand and the style your logo design should communicate.

```html
<!DOCTYPE html>
<html lang="en">
<head>
<meta charset="utf-8">
<title>The Ember Vale — Business Card</title>
<link rel="stylesheet" href="https://fonts.googleapis.com/css2?family=Jost:wght@300;400;500;600&display=swap">
<style>
  :root {
    --backdrop: #e9e6e2;
    --card: #222324;
    --card-edge: #2b2c2d;
    --gold: #e5b51f;
    --ink-light: #f1f1f1;
    --ink-muted: #8e9194;
  }
  * { box-sizing: border-box; margin: 0; padding: 0; }
  html, body { width: 1200px; height: 880px; overflow: hidden; }
  body {
    background: var(--backdrop);
    font-family: "Jost", "Helvetica Neue", Arial, sans-serif;
    position: relative;
  }
  .card {
    position: absolute;
    left: 320px;
    width: 560px;
    height: 320px;
    background: var(--card);
    border: 1px solid var(--card-edge);
    overflow: hidden;
  }
  .card--details { top: 90px; }
  .card--brand { top: 470px; }

  .brand-lockup {
    position: absolute;
    display: flex;
    align-items: center;
    gap: 12px;
  }
  .brand-lockup__dot {
    width: 26px; height: 26px;
    border-radius: 50%;
    background: var(--gold);
    flex: none;
  }
  .brand-lockup__name {
    font-weight: 500;
    font-size: 26px;
    letter-spacing: 0.04em;
    color: var(--ink-light);
    text-transform: uppercase;
    white-space: nowrap;
  }

  /* details side */
  .accent-vertical {
    position: absolute;
    left: 92px; top: 0;
    width: 5px; height: 150px;
    background: var(--gold);
  }
  .card--details .brand-lockup { right: 34px; top: 112px; }
  .card--details .brand-lockup__name { font-size: 22px; }

  .holder {
    position: absolute;
    left: 40px; top: 170px;
    display: flex; align-items: baseline; gap: 8px;
  }
  .holder__name { color: var(--gold); font-weight: 600; font-size: 21px; }
  .holder__role { color: var(--ink-light); font-weight: 300; font-size: 14px; }

  .contact-list {
    position: absolute;
    list-style: none;
    color: var(--ink-light);
    font-size: 13.5px;
    font-weight: 400;
    line-height: 22px;
  }
  .contact-list li { display: flex; align-items: center; gap: 8px; }
  .contact-list svg { width: 12px; height: 12px; fill: var(--gold); flex: none; }
  .contact-list--phones { left: 40px; top: 206px; }
  .contact-list--online { left: 232px; top: 228px; }

  .accent-edge {
    position: absolute;
    left: 20px; top: 208px;
    width: 3px; height: 44px;
    background: var(--gold);
  }
  .accent-horizontal {
    position: absolute;
    left: 40px; top: 282px;
    width: 340px; height: 2px;
    background: var(--gold);
  }

  /* brand side */
  .card--brand .brand-lockup {
    left: 50%; top: 120px;
    transform: translateX(-50%);
  }
  .card--brand .brand-lockup__name { font-size: 30px; }
  .website {
    position: absolute;
    left: 0; right: 0; bottom: 30px;
    text-align: center;
    color: var(--ink-muted);
    font-size: 15px;
    font-weight: 400;
    letter-spacing: 0.12em;
  }
  .website strong { font-weight: 600; }
</style>
</head>
<body>

<section class="card card--details" aria-label="Card side with contact details">
  <div class="accent-vertical"></div>

  <div class="brand-lockup">
    <span class="brand-lockup__dot"></span>
    <span class="brand-lockup__name">The Ember Vale</span>
  </div>

  <div class="holder">
    <span class="holder__name">Name Surname</span>
    <span class="holder__role">/manager</span>
  </div>

  <div class="accent-edge"></div>
  <ul class="contact-list contact-list--phones">
    <li>
      <svg viewBox="0 0 12 12" aria-hidden="true"><rect x="2" y="0" width="8" height="12" rx="1.5"/></svg>
      +1 555 014 3945
    </li>
    <li>
      <svg viewBox="0 0 12 12" aria-hidden="true"><path d="M2 1h3l1 3-2 1a7 7 0 0 0 3 3l1-2 3 1v3a1 1 0 0 1-1 1A10 10 0 0 1 1 2a1 1 0 0 1 1-1z"/></svg>
      +1 555 018 7892
    </li>
  </ul>

  <ul class="contact-list contact-list--online">
    <li>
      <svg viewBox="0 0 12 12" aria-hidden="true"><path d="M0 2h12v8H0zM1 3l5 4 5-4" stroke="#222324" stroke-width="1"/></svg>
      hello@embervale.example
    </li>
    <li>
      <svg viewBox="0 0 12 12" aria-hidden="true"><circle cx="6" cy="6" r="6"/><path d="M0 6h12M6 0v12" stroke="#222324" stroke-width="1"/></svg>
      www.embervale.example
    </li>
  </ul>

  <div class="accent-horizontal"></div>
</section>

<section class="card card--brand" aria-label="Card side with company name">
  <div class="brand-lockup">
    <span class="brand-lockup__dot"></span>
    <span class="brand-lockup__name">The Ember Vale</span>
  </div>
  <p class="website">www.<strong>embervale</strong>.example</p>
</section>

</body>
</html>
```